Restaurant needs a vertical banner for fried catfish

Our restaurant is looking for an eye-catching 78.75in. x 36in. vertical physical banner ad for our fried catfish. Photos for the fried catfish will be provided as a reference but we will also accept anything similar to the photo. We will be using the following as our receptacle: https://www.plankoria.example/banner-stand/retractable-banner-stands/
The design must incorporate the following flavor texts:
Fried Catfish
Always Fresh!
Made from Scratch
Hand-cut Fillets
The Best Catfish in Texas
Served with fries, hush puppies, and a 32oz fountain drink
Also available by the pound!
The final design should be creative, professional, and eye-catching for customers.
Updates
Colors
Designer to choose colors to be used in the design.
Requirements
Must have
- We are open to any and all design elements, albeit the 'flavor texts' should not overpower, but complement the fried catfish photo. 'Fried Catfish' can be used in lieu of a main title/logo.
Nice to have
- Transparent or textured backgrounds that can encompass any or all part of the banner such as a cutting board, shadows, abstract, etc to show depth are a plus.
- Use of vectors or objects such as ribbons or shapes to encapsulate the 'flavor texts' are also encouraged.

```html
<!DOCTYPE html>
<html lang="en">
<head>
<meta charset="utf-8">
<title>Fried Catfish Banner</title>
<link rel="stylesheet" href="https://fonts.googleapis.com/css2?family=Archivo:wght@500;800&family=Lato:wght@400&display=swap">
<style>
  :root {
    --yellow: #ffe000;
    --olive-dark: #3b3304;
    --olive-mid: #8a7a02;
    --gold: #f0d400;
    --blue: #0a3cf0;
    --navy: #101a4c;
    --panel-top: #1c2434;
    --panel-bottom: #0d1526;
    --white: #ffffff;
  }
  * { margin: 0; padding: 0; box-sizing: border-box; }
  html, body { width: 1200px; height: 2625px; overflow: hidden; }
  body { position: relative; background: var(--yellow); font-family: "Lato", sans-serif; }

  .stage {
    position: absolute; left: 0; top: 253px; width: 1200px; height: 2129px;
    background: linear-gradient(180deg, var(--olive-dark) 0%, var(--olive-mid) 22%, var(--gold) 45%, var(--yellow) 75%);
  }
  .corner-shapes { position: absolute; left: 0; top: 0; width: 1200px; height: 2625px; }

  .top-band {
    position: absolute; left: 0; top: 0; width: 1200px; height: 253px;
    background: var(--yellow); box-shadow: 0 12px 24px rgba(0,0,0,.35); z-index: 2;
  }
  .main-title {
    position: absolute; left: 0; right: 0; top: 48px; text-align: center;
    font-family: "Archivo", sans-serif; font-weight: 800; font-size: 122px;
    letter-spacing: 12px; color: var(--blue); line-height: 1;
  }

  .photo {
    position: absolute; border-radius: 14px;
    box-shadow: 0 10px 26px rgba(0,0,0,.4);
  }
  .photo-basket { left: 201px; top: 362px; width: 346px; height: 346px; background: linear-gradient(160deg, #d9cdbb, #c79a52 55%, #e7e2da); }
  .photo-board { left: 203px; top: 778px; width: 346px; height: 346px; background: linear-gradient(150deg, #4a2c1c, #d59a3e 50%, #3a2318); }
  .photo-hand { left: 651px; top: 362px; width: 347px; height: 762px; background: linear-gradient(180deg, #b9a99a, #d9a070 40%, #b8652a 75%, #2e2a2a); }

  .info-panel {
    position: absolute; left: 132px; top: 1189px; width: 943px; height: 1193px;
    background: radial-gradient(ellipse at 55% 65%, #3b3428 0%, var(--panel-top) 45%, var(--panel-bottom) 100%);
  }
  .panel-title {
    position: absolute; left: 248px; top: 1296px;
    font-family: "Archivo", sans-serif; font-weight: 500; font-size: 84px;
    letter-spacing: 11px; color: var(--white); line-height: 1;
  }
  .feature-list { list-style: none; }
  .feature {
    position: absolute; left: 173px; color: var(--white);
    font-size: 73px; line-height: 85px;
  }
  .feature svg { position: absolute; left: 0; top: 23px; width: 56px; height: 44px; }
  .feature span { display: block; margin-left: 97px; }

  .bottom-band {
    position: absolute; left: 0; top: 2382px; width: 1200px; height: 243px;
    background: var(--yellow); box-shadow: 0 -8px 20px rgba(0,0,0,.25);
  }
  .pound-note {
    position: absolute; left: 0; right: 0; top: 37px; text-align: center;
    font-family: "Archivo", sans-serif; font-weight: 500; font-size: 64px;
    letter-spacing: 6px; color: var(--navy); line-height: 1;
  }
</style>
</head>
<body>
  <div class="stage"></div>
  <svg class="corner-shapes" viewBox="0 0 1200 2625" aria-hidden="true">
    <polygon points="0,253 336,253 0,535" fill="var(--yellow)"/>
  </svg>

  <header class="top-band">
    <h1 class="main-title">FRIED CATFISH</h1>
  </header>

  <div class="photo photo-basket" role="img" aria-label="Fried catfish strips in a wire basket with parsley"></div>
  <div class="photo photo-board" role="img" aria-label="Breaded catfish fillets on a wooden board with grilled lemon"></div>
  <div class="photo photo-hand" role="img" aria-label="Hand picking up a crispy fried catfish strip with dipping sauce"></div>

  <div class="info-panel" role="img" aria-label="Plate of fried catfish with chips and tartar sauce, darkened"></div>
  <svg class="corner-shapes" viewBox="0 0 1200 2625" aria-hidden="true">
    <polygon points="1200,2094 1200,2382 866,2382" fill="var(--yellow)"/>
  </svg>

  <h2 class="panel-title">FRIED CATFISH</h2>
  <ul class="feature-list">
    <li class="feature" style="top:1437px"><svg viewBox="0 0 56 44"><path d="M0 0 L56 22 L0 44 L12 22 Z" fill="#fff"/></svg><span>Fried Catfish</span></li>
    <li class="feature" style="top:1544px"><svg viewBox="0 0 56 44"><path d="M0 0 L56 22 L0 44 L12 22 Z" fill="#fff"/></svg><span style="margin-left:93px">Always Fresh!</span></li>
    <li class="feature" style="top:1657px"><svg viewBox="0 0 56 44"><path d="M0 0 L56 22 L0 44 L12 22 Z" fill="#fff"/></svg><span style="margin-left:93px">Made From Scratch</span></li>
    <li class="feature" style="top:1771px"><svg viewBox="0 0 56 44"><path d="M0 0 L56 22 L0 44 L12 22 Z" fill="#fff"/></svg><span style="margin-left:93px">Hand-Cut Fillets</span></li>
    <li class="feature" style="top:1900px"><svg viewBox="0 0 56 44"><path d="M0 0 L56 22 L0 44 L12 22 Z" fill="#fff"/></svg><span>The Best Catfish in Texas</span></li>
    <li class="feature" style="top:2017px"><svg viewBox="0 0 56 44"><path d="M0 0 L56 22 L0 44 L12 22 Z" fill="#fff"/></svg><span>Served With Fries,<br>Hush Puppies, and a<br>32ozFountain Drinks</span></li>
  </ul>

  <footer class="bottom-band">
    <p class="pound-note">Also Available by the Pound!</p>
  </footer>
</body>
</html>
```